International sourcing and trading company needs website design on Squarespace

We are international sourcing and trading company based in Brisbane ,Australia. We help our clients to source any products they need to economically produce overseas and we manage the whole production process for them. We want our visual identity to show that we are professional, dynamic, efficient and are able to source any product around the world. Our website will be simply information and advertising website , no ecommerce or any transactions. Please see attached our company logo. We would like our website to have the following sections/pages:

1.Main banner with a simple slogan/sentence to introduce what we do: Let us handle the overseas sourcing and production for you.

2. Post-Covid sourcing and producing management: introducing our competence on managing sourcing and overseas production under the travel restriction and the growing tension on global trading. We will supply the exact wording later on;

3. About us: We are a professional team with mature global sourcing and trading experience. We have branch office in Hong Kong and local resources around all areas in China , India and other Asian countries. Our working flow is: received inquiry->start sourcing->(in 1 week time)give price and delivery date on inquired products or further information->(if needed)arrange samples for clients->(if samples and orders are confirmed)deliver Pre-production sample-> kick-off production->arrange inspection through the whole production-> (if need) arrange shipment to client. We would like to show the work flow in a personalized way , eg. personalize icons etc.;

4. What kind of product we can source and produce: our business is sourcing and managing manufacture overseas for our clients, product categories mainly, but not just, are clothing, shoes , bags, clothing accessories, makeup accessories, festival or promotional gifts etc. all kind of daily use products . We basically are able to source and manage production of every kind of products with no limits. We would like this page to be particularly personalized in a way to give impression to whom browse our website feel free to send inquiry of any kind of production to us and they can trust us that we will do our job professionally and dynamically. We are thinking of using some icons of daily use products to show our sourcing category , it's just our though so please feel free to propose any other ides that you think is more suitable from the point of view of professional designer.

5. Start an enquiry: here we need to land on a questionary page to let who would like to make en enquiry leave the main information , including:
-Name & Sir name:
-Company name:
-Contact email:
-Phone numer:
-Enquired product:
-Upload image:
-Preferred or previous production country:
-Preferred price: FOB, CIF, DDP
-If CIF or DDP where the arrival port/airport will be:
-Preferred delivery time:
-Preferred transportation: by air, by sea, by train
- Other specific requires:

6: Contact us: We will supply contact info later on

Above are our thoughts but please feel free to propose any other ideas that you think should be more suitable for us. We trust your expertise and professional opinions.

Target Market(s)

Wholesalers and retailers who need to produce their products overseas (mainly in China and other countries in Asia)

Coding

Coded - Design and coding required

Font styles to use
Sans Serif

Requirements
Nice to have
• We think it will be nice to show information in simple and comprehensive icons instead of piles of words. We will want our website neat, easy to understand what we do and professional. However this is just our thought so please feel free to propose any other ideas that you think is more suitable from the point of view of professional designer.

```html
<!DOCTYPE html>
<html lang="en">
<head>
<meta charset="utf-8">
<title>CargoLoom – Global sourcing and trading</title>
<link href="https://fonts.googleapis.com/css2?family=Nunito+Sans:wght@300;400;600;700&display=swap" rel="stylesheet">
<style>
:root{
  --orange:#f5a84a;
  --ink:#111111;
  --text:#222222;
  --muted:#8a8a8a;
  --line:#c9c9c9;
  --soft:#f4f4f4;
  --teal:#3fb0c9;
  --footer:#151515;
}
*{box-sizing:border-box;margin:0;padding:0}
html,body{width:1200px;height:3838px;overflow:hidden}
body{font-family:"Nunito Sans",sans-serif;color:var(--text);background:#fff;position:relative}
.abs{position:absolute}
.btn{position:absolute;background:var(--orange);color:#fff;border-radius:30px;display:flex;align-items:center;justify-content:center;font-weight:600}

/* notice bar */
.notice{left:0;top:0;width:1200px;height:82px;background:var(--ink);color:#fff}
.notice p{position:absolute;left:90px;top:18px;font-size:13.5px;line-height:23px;width:720px}
.notice .close{position:absolute;right:18px;top:14px;font-size:14px}

/* header */
.brand{position:absolute;display:flex;align-items:center;gap:12px}
.brand .dot{width:62px;height:62px;border-radius:50%;background:var(--teal)}
.brand .name{font-weight:700;color:var(--orange);line-height:1}
.brand .tag{display:block;font-size:17px;font-weight:600;color:var(--orange);margin-top:6px}
.header-mail{left:958px;top:96px;font-size:15px;display:flex;align-items:center;gap:8px}
.nav{left:514px;top:132px;display:flex;gap:40px;font-size:16px}
.nav .active{color:var(--orange)}

/* hero */
.hero{left:0;top:167px;width:1200px;height:628px;background:linear-gradient(180deg,#6e6a66 0%,#4d4a4a 45%,#2e2d31 100%)}
.hero h1{position:absolute;left:0;top:200px;width:1200px;text-align:center;color:#fff;font-size:55px;font-weight:600;line-height:61px}

/* about */
.about-art{left:90px;top:887px;width:521px;height:417px;border-radius:50%;background:radial-gradient(circle at 45% 45%,#d8c2a3,#9c8068 55%,#3b3432 100%)}
.about h2{position:absolute;left:689px;top:945px;font-size:55px;font-weight:600;color:var(--ink)}
.about p{position:absolute;left:689px;top:1026px;width:430px;font-size:16px;line-height:31.5px}

/* flow */
.section-title{position:absolute;left:0;width:1200px;text-align:center;font-size:55px;font-weight:600;color:var(--ink)}
.flow-mark{left:566px;top:1483px;width:86px;height:67px;border-radius:50%;background:linear-gradient(135deg,var(--teal),var(--orange))}
.flow-line{left:598px;top:1557px;height:845px;border-left:1.5px dashed var(--line)}
.step{position:absolute;width:440px;height:113px;background:#fff;box-shadow:0 2px 10px rgba(0,0,0,.09);padding:16px 22px}
.step::after{content:"";position:absolute;top:40px;width:18px;height:18px;background:#fff;transform:rotate(45deg);box-shadow:2px -2px 4px rgba(0,0,0,.05)}
.step.left::after{right:-9px}
.step.right::after{left:-9px;box-shadow:-2px 2px 4px rgba(0,0,0,.05)}
.step h3{font-size:17px;font-weight:400;color:var(--text);display:flex;align-items:flex-start;gap:10px;line-height:25px}
.step h3 svg{flex:none;margin-top:5px}
.step p{font-size:14.5px;color:var(--muted);line-height:25px;margin-top:4px}

/* products */
.cats{left:89px;top:2554px;width:248px}
.cats h4{height:45px;background:var(--orange);color:#fff;font-size:21px;font-weight:600;padding:8px 18px}
.cats li{list-style:none;height:46.5px;background:var(--soft);border-bottom:1px solid #fff;font-size:15.5px;color:#666;padding:12px 18px}
.prod{position:absolute;top:2554px;width:248px;height:325px;border:3px solid var(--orange);background:var(--orange)}
.prod .pic{height:245px}
.prod h5{color:#fff;font-size:22px;font-weight:600;padding:6px 6px 0;line-height:26px}
.prod span{color:#fff;font-size:13px;padding-left:8px}

/* enquiry */
.enquiry{left:0;top:3032px;width:1200px;height:351px;background:linear-gradient(90deg,#4a4c57 0%,#7c7a80 40%,#3c4a66 75%,#28344e 100%)}
.enquiry h2{position:absolute;left:0;top:86px;width:1200px;text-align:center;color:#fff;font-size:55px;font-weight:600}
.enquiry p{position:absolute;left:0;top:162px;width:1200px;text-align:center;color:#fff;font-size:16px}

/* footer */
.footer{left:0;top:3383px;width:1200px;height:455px;background:var(--footer);color:#fff}
.footer h4{position:absolute;top:84px;font-size:21px;font-weight:700}
.footer ul{position:absolute;top:140px;list-style:none;font-size:14px;line-height:31.5px}
.socials{position:absolute;left:106px;top:200px;display:flex;gap:28px}
.socials span{width:14px;height:14px;border-radius:50%;background:#fff}
.news-input{position:absolute;left:852px;top:215px;width:255px;height:36px;background:#fff;color:#777;font-size:13.5px;padding:9px 14px}
.news-btn{position:absolute;left:852px;top:260px;width:255px;height:36px;background:var(--orange);color:#fff;font-size:17px;font-weight:600;text-align:center;line-height:36px}
.copy{position:absolute;left:0;top:418px;width:1200px;text-align:center;font-size:12px}
</style>
</head>
<body>

<div class="abs notice">
  <p>Post-Covid sourcing and producing management: introducing our competence on managing sourcing and overseas production under the travel restriction and the growing tension on global trading.</p>
  <span class="close">x</span>
</div>

<div class="brand" style="left:90px;top:95px">
  <span class="dot"></span>
  <span class="name" style="font-size:38px">CargoLoom<span class="tag">Global sourcing and trading</span></span>
</div>
<div class="abs header-mail">
  <svg width="16" height="12" viewBox="0 0 16 12"><rect width="16" height="12" rx="1" fill="#f5a84a"/><path d="M1 1l7 6 7-6" stroke="#fff" stroke-width="1.5" fill="none"/></svg>
  hello@cargoloom.example
</div>
<nav class="abs nav">
  <span class="active">Home</span><span>About Us</span><span>Products</span><span>Categories</span><span>Enquiry</span><span>Contact Us</span>
</nav>

<section class="abs hero" role="img" aria-label="Photo of a clothing store interior with garments on rails">
  <h1>Let us handle the overseas sourcing<br>and production for you.</h1>
</section>
<a class="btn" style="left:500px;top:525px;width:200px;height:58px;font-size:22px">Get Started</a>

<section class="about">
  <div class="abs about-art" role="img" aria-label="Globe-shaped collage of clothing photos in swept bands"></div>
  <h2>About us</h2>
  <p>We are a professional team with mature global sourcing and trading experience.We have branch office in Hong Kong and local resources around all areas in China , India and other Asian countries.</p>
  <a class="btn" style="left:689px;top:1186px;width:164px;height:49px;font-size:17px">Contact Us</a>
</section>

<h2 class="section-title" style="top:1385px">Our working flow</h2>
<div class="abs flow-mark"></div>
<div class="abs flow-line"></div>

<div class="step left" style="left:131px;top:1596px"><h3><svg width="15" height="13" viewBox="0 0 15 13"><rect x="1" y="2" width="10" height="10" fill="none" stroke="#3fb0c9" stroke-width="1.6"/><path d="M4 6l3 3 7-8" stroke="#3fb0c9" stroke-width="1.8" fill="none"/></svg>Received Inquiry</h3><p>Lorem ipsum dolor sit amet, consectetur adipiscing elit, sed do eiusmod tempor incididunt ut.</p></div>
<div class="step right" style="left:629px;top:1703px"><h3><svg width="15" height="13" viewBox="0 0 15 13"><rect x="1" y="2" width="10" height="10" fill="none" stroke="#3fb0c9" stroke-width="1.6"/><path d="M4 6l3 3 7-8" stroke="#3fb0c9" stroke-width="1.8" fill="none"/></svg>Start Sourcing</h3><p>Lorem ipsum dolor sit amet, consectetur adipiscing elit, sed do eiusmod tempor incididunt ut.</p></div>
<div class="step left" style="left:131px;top:1784px"><h3><svg width="15" height="13" viewBox="0 0 15 13"><rect x="1" y="2" width="10" height="10" fill="none" stroke="#3fb0c9" stroke-width="1.6"/><path d="M4 6l3 3 7-8" stroke="#3fb0c9" stroke-width="1.8" fill="none"/></svg>Further Information</h3><p>Lorem ipsum dolor sit amet, consectetur adipiscing elit, sed do eiusmod tempor incididunt ut.</p></div>
<div class="step right" style="left:629px;top:1891px"><h3><svg width="15" height="13" viewBox="0 0 15 13"><rect x="1" y="2" width="10" height="10" fill="none" stroke="#3fb0c9" stroke-width="1.6"/><path d="M4 6l3 3 7-8" stroke="#3fb0c9" stroke-width="1.8" fill="none"/></svg>Deliver Pre-production Sample</h3><p>Lorem ipsum dolor sit amet, consectetur adipiscing elit, sed do eiusmod tempor incididunt ut.</p></div>
<div class="step left" style="left:131px;top:1973px"><h3><svg width="15" height="13" viewBox="0 0 15 13"><rect x="1" y="2" width="10" height="10" fill="none" stroke="#3fb0c9" stroke-width="1.6"/><path d="M4 6l3 3 7-8" stroke="#3fb0c9" stroke-width="1.8" fill="none"/></svg>Kick-off Production</h3><p>Lorem ipsum dolor sit amet, consectetur adipiscing elit, sed do eiusmod tempor incididunt ut.</p></div>
<div class="step right" style="left:629px;top:2080px"><h3><svg width="15" height="13" viewBox="0 0 15 13"><rect x="1" y="2" width="10" height="10" fill="none" stroke="#3fb0c9" stroke-width="1.6"/><path d="M4 6l3 3 7-8" stroke="#3fb0c9" stroke-width="1.8" fill="none"/></svg>Arrange Inspection Through The Whole Production</h3><p>Lorem ipsum dolor sit amet, consectetur adipiscing</p></div>
<div class="step left" style="left:131px;top:2161px"><h3><svg width="15" height="13" viewBox="0 0 15 13"><rect x="1" y="2" width="10" height="10" fill="none" stroke="#3fb0c9" stroke-width="1.6"/><path d="M4 6l3 3 7-8" stroke="#3fb0c9" stroke-width="1.8" fill="none"/></svg>Arrange Shipment To Client</h3><p>Lorem ipsum dolor sit amet, consectetur adipiscing elit, sed do eiusmod tempor incididunt ut.</p></div>
<div class="step right" style="left:629px;top:2268px;padding-top:30px"><p>We would like to show the work flow in a personalized way , eg. personalize icons etc.;</p></div>

<h2 class="section-title" style="top:2470px">Our Products</h2>
<div class="abs cats">
  <h4>Categories</h4>
  <ul>
    <li>Clothing</li><li>Shoes</li><li>Bags</li><li>Clothing Accessories</li><li>Makeup Accessories</li><li>Festival Or Promotional Gifts</li>
  </ul>
</div>
<div class="prod" style="left:344px"><div class="pic" role="img" aria-label="Flat lay of women's clothing, heels and accessories" style="background:linear-gradient(135deg,#f6f3ef,#e3ddd5)"></div><h5>Clothing</h5><span>Lorem ipsum dolor</span></div>
<div class="prod" style="left:603px"><div class="pic" role="img" aria-label="Pair of white and blue running shoes" style="background:radial-gradient(circle at 50% 55%,#dfe3ea,#ffffff 70%)"></div><h5>Shoes</h5><span>Lorem ipsum dolor</span></div>
<div class="prod" style="left:861px"><div class="pic" role="img" aria-label="Yellow backpack" style="background:radial-gradient(circle at 50% 50%,#f4c43a,#ffffff 55%)"></div><h5>Bags</h5><span>Lorem ipsum dolor</span></div>
<a class="btn" style="left:517px;top:2891px;width:164px;height:48px;font-size:18px">View All</a>

<section class="abs enquiry" role="img" aria-label="Blurred photo of jeans hanging on a clothing rail">
  <h2>Start an enquiry</h2>
  <p>Lorem ipsum dolor sit amet, consectetur adipiscing elit, sed do eiusmod tempor incididunt ut labore et dolore magna aliqua.</p>
</section>
<a class="btn" style="left:517px;top:3241px;width:164px;height:46px;font-size:18px">Contact Us</a>

<footer class="abs footer">
  <div class="brand" style="left:90px;top:68px;flex-direction:column;align-items:flex-start;gap:8px">
    <span class="dot" style="width:44px;height:44px;margin-left:60px"></span>
    <span class="name" style="font-size:32px">CargoLoom<span class="tag" style="font-size:14px;margin-top:3px">Global sourcing and trading</span></span>
  </div>
  <div class="socials"><span></span><span></span><span></span><span></span></div>
  <h4 style="left:407px">Links</h4>
  <ul style="left:407px"><li>Home</li><li>About Us</li><li>Products</li><li>Categories</li><li>Enquiry</li><li>Contact Us</li></ul>
  <h4 style="left:591px">Contact Us</h4>
  <ul style="left:591px"><li>Lorem ipsum dolor sit amet,</li><li>consectetur adipiscing</li><li>&nbsp;</li><li>+8 888 888 888</li><li>&nbsp;</li><li>hello@cargoloom.example</li></ul>
  <h4 style="left:852px">Newsletter</h4>
  <ul style="left:852px"><li>Lorem ipsum dolor sit amet,</li><li>consectetur adipiscing</li></ul>
  <div class="news-input">Enter Your Email Address</div>
  <div class="news-btn">Subscribe</div>
  <p class="copy">© Copyrights.2020.The Company Name.All Rights Reserved</p>
</footer>

</body>
</html>
```